Business Card Design Project

Business Card
We are rebranding with a new logo
Industry/Entity Type
Business
Contact Information for Business Card
Dennis Marlow +61 427581962 dennis@qovo.com.au P.O. Box 872 Kelvindale QLD 4309
Requirements
Must have
- Logo

```html
<!DOCTYPE html>
<html lang="en">
<head>
<meta charset="utf-8">
<title>Qovo International – Business Card</title>
<link href="https://fonts.googleapis.com/css2?family=Poppins:wght@400;600&display=swap" rel="stylesheet">
<style>
  :root {
    --deep-blue: #127fa8;
    --sky-blue: #22aae2;
    --orange: #f58b20;
    --red-orange: #e86426;
    --ink: #1a1a1a;
    --paper: #ffffff;
  }
  * { margin: 0; padding: 0; box-sizing: border-box; }
  html, body { width: 1193px; height: 1200px; overflow: hidden; }
  body { position: relative; background: var(--paper); font-family: "Poppins", sans-serif; color: var(--ink); }

  .backdrop-orange { position: absolute; left: 0; top: 600px; width: 1193px; height: 600px; background: var(--orange); }

  .card { position: absolute; left: 352px; width: 518px; height: 295px; background: var(--paper); overflow: hidden; }
  .card-front { top: 157px; }
  .card-back { top: 748px; }

  .band { position: absolute; }
  .band-top { left: 0; top: 0; width: 484px; height: 35px; background: var(--deep-blue); }
  .band-right { left: 484px; top: 0; width: 34px; height: 261px; background: var(--orange); }
  .band-left { left: 0; top: 35px; width: 35px; height: 260px; background: var(--red-orange); }
  .band-bottom { left: 35px; top: 261px; width: 483px; height: 34px; background: var(--sky-blue); }

  .brand-name {
    position: absolute;
    font-weight: 600;
    font-size: 21px;
    color: var(--deep-blue);
    line-height: 1.05;
    letter-spacing: 0.04em;
    white-space: nowrap;
  }
  .card-front .brand-name { left: 71px; top: 158px; }
  .card-back .brand-name { left: 93px; top: 84px; }

  .contact { position: absolute; list-style: none; }
  .contact li { white-space: nowrap; letter-spacing: 0.16em; }
  .contact .name { text-transform: uppercase; }
  .card-front .contact { right: 58px; top: 53px; text-align: right; font-size: 10.5px; }
  .card-front .contact li { height: 22.7px; }
  .card-back .contact { left: 267px; top: 97px; font-size: 7.6px; }
  .card-back .contact li { height: 16.6px; }

  .swatches { position: absolute; left: 0; top: 207px; width: 518px; height: 44px; }
  .swatch { position: absolute; top: 0; width: 44px; height: 44px; border-radius: 50%; border: 4.5px solid; }
  .swatch-1 { left: 69px; border-color: var(--orange); background: var(--deep-blue); }
  .swatch-2 { left: 182px; border-color: var(--sky-blue); background: var(--orange); }
  .swatch-3 { left: 293px; border-color: var(--red-orange); background: var(--sky-blue); }
  .swatch-4 { left: 405px; border-color: var(--deep-blue); background: var(--red-orange); }
</style>
</head>
<body>
  <div class="backdrop-orange"></div>

  <section class="card card-front">
    <div class="band band-top"></div>
    <div class="band band-right"></div>
    <div class="band band-left"></div>
    <div class="band band-bottom"></div>
    <div class="brand-name">Qovo<br>International</div>
    <ul class="contact">
      <li class="name">Dennis Marlow</li>
      <li>+61 427581962</li>
      <li>dennis@qovo.com.au</li>
      <li>P.O. Box 872 Kelvindale QLD 4309</li>
    </ul>
  </section>

  <section class="card card-back">
    <div class="brand-name">Qovo<br>International</div>
    <ul class="contact">
      <li class="name">Dennis Marlow</li>
      <li>+61 427581962</li>
      <li>dennis@qovo.com.au</li>
      <li>P.O. Box 872 Kelvindale QLD 4309</li>
    </ul>
    <div class="swatches">
      <span class="swatch swatch-1"></span>
      <span class="swatch swatch-2"></span>
      <span class="swatch swatch-3"></span>
      <span class="swatch swatch-4"></span>
    </div>
  </section>
</body>
</html>
```